Business Card Design

I do estate sales and would like business card to reflect look and feel of attached logo. I also have copy of logo in .eps and .tif if you need that instead of .jpeg.
Updates

sorry for the delay in reviewing these designs. I will pick one by tomorrow. Here are the absolutes: *must have tagline (we find good homes for your treasures *must use blue and green *must be horizontal *nothing too fancy please submit your best and final. Thanks so much!

Industry/Entity Type

Business

Contact Information for Business Card

Nora Platt

DEALS by NORA
We find good homes for your treasures.

Specializing in one to three-day sales
o (no sale too big or too small)
• Home and garage organizing
• Home Clean-out

Call Nora Platt at 202-555-0187
to schedule.

```html
<!DOCTYPE html>
<html lang="en">
<head>
<meta charset="utf-8">
<title>Deals by Nora – Business Card</title>
<link rel="stylesheet" href="https://fonts.googleapis.com/css2?family=Alegreya:wght@400;700&display=swap">
<style>
  :root {
    --brand-green: #5a9510;
    --brand-blue: #2a98b5;
    --card-white: #ffffff;
    --ink: #141414;
  }
  html, body {
    margin: 0;
    padding: 0;
    width: 1200px;
    height: 703px;
    overflow: hidden;
    background: var(--card-white);
  }
  .card {
    position: relative;
    width: 1200px;
    height: 703px;
    background: var(--card-white);
    font-family: "Alegreya", Georgia, serif;
    font-variant-numeric: lining-nums;
    color: var(--ink);
  }
  .edge-left {
    position: absolute;
    left: 0;
    top: 0;
    width: 59px;
    height: 703px;
    background: var(--brand-green);
  }
  .edge-bottom {
    position: absolute;
    left: 0;
    top: 646px;
    width: 1200px;
    height: 57px;
    background: var(--brand-green);
  }
  .brand {
    position: absolute;
    left: 160px;
    top: 318px;
    width: 390px;
    height: 66px;
    display: flex;
    align-items: center;
    gap: 14px;
  }
  .brand-dot {
    flex: none;
    width: 26px;
    height: 26px;
    border-radius: 50%;
    background: var(--brand-blue);
  }
  .brand-name {
    margin: 0;
    font-size: 52px;
    font-weight: 400;
    line-height: 1;
    color: var(--brand-green);
    white-space: nowrap;
  }
  .contact {
    position: absolute;
    left: 703px;
    top: 196px;
  }
  .contact-name {
    margin: 0;
    font-size: 37px;
    font-weight: 700;
    letter-spacing: 2.5px;
    line-height: 1.1;
  }
  .contact-phone {
    margin: 6px 0 0;
    font-size: 37px;
    font-weight: 400;
    letter-spacing: 2px;
    line-height: 1.1;
  }
  .services {
    position: absolute;
    left: 703px;
    top: 366px;
    font-size: 28px;
    letter-spacing: 0.7px;
    line-height: 35.5px;
    white-space: nowrap;
  }
  .services-tagline {
    margin: 0;
  }
  .services-list {
    list-style: none;
    margin: 0;
    padding: 0;
  }
  .services-list li::before {
    content: "\2022\00a0";
  }
</style>
</head>
<body>
  <main class="card">
    <div class="edge-left"></div>
    <div class="edge-bottom"></div>

    <div class="brand">
      <span class="brand-dot"></span>
      <p class="brand-name">Deals by Nora</p>
    </div>

    <section class="contact">
      <h1 class="contact-name">Nora Platt</h1>
      <p class="contact-phone">202-555-0187</p>
    </section>

    <section class="services">
      <p class="services-tagline">Finds good homes for your treasures</p>
      <ul class="services-list">
        <li>specializing in 1-3-day sales</li>
        <li>home and garage organizing</li>
        <li>home Clean-out</li>
      </ul>
    </section>
  </main>
</body>
</html>
```